Corwenna Foundation is a new grant making charity set up in the UK.

Having got a logo, we now need a website to go with it. We have worked out the text which people are going to need in order to then apply for grants. But having found out what we require they will probably need to go away and think about it.
We have to be careful of what images we use. So I have uploaded some images that we like. We are also going to be adding more pages almost immediately so need to think about the images for these.
I know basic wordpress so I will be able to add new pages/make alterations in future.
Updates
The website does need to be coded in Wordpress so that I can maintain it afterwards.
Corwenna
Brief changed to provide more money and we have also provided more possible pictures. And generally more explanation.
Target Market(s)
departments in universities, other charities doing work on relief of pain, people working in health service departments
Industry/Entity Type
Health Charity
Coding
Coded - Design and coding required
Number of Pages Required
4 page
Look and feel
Each slider illustrates characteristics of the customer's brand and the style your logo design should communicate.

```html
<!DOCTYPE html>
<html lang="en">
<head>
<meta charset="utf-8">
<title>Grants – Corwenna Foundation</title>
<link href="https://fonts.googleapis.com/css2?family=Montserrat:wght@400;500;600;700;800&family=Roboto:wght@400&display=swap" rel="stylesheet">
<style>
  :root {
    --brand-blue: #1470bf;
    --heading-blue: #1a6fb8;
    --ink: #2b2b2b;
    --body-text: #5a5a5a;
    --white: #ffffff;
    --footer-bg: #1c1c1c;
    --footer-rule: #3a3a3a;
    --hero-dark: #4a4240;
    --hero-mid: #7a6058;
    --hero-warm: #b88b7c;
  }
  * { margin: 0; padding: 0; box-sizing: border-box; }
  html, body { width: 1200px; height: 795px; overflow: hidden; background: var(--white); }
  body { position: relative; font-family: "Roboto", sans-serif; }

  .hero {
    position: absolute; left: 0; top: 0; width: 1200px; height: 329px;
    background:
      radial-gradient(ellipse 360px 220px at 780px 170px, var(--hero-warm) 0%, rgba(184,139,124,0.4) 55%, transparent 100%),
      linear-gradient(90deg, var(--hero-dark) 0%, #5a4c48 40%, var(--hero-mid) 65%, #8a6a62 100%);
  }
  .header-panel { position: absolute; left: 0; top: 0; width: 420px; height: 77px; }
  .header-rule { position: absolute; left: 372px; top: 76px; width: 828px; height: 1px; background: rgba(255,255,255,0.45); }

  .brand { position: absolute; left: 183px; top: 22px; display: flex; align-items: center; gap: 8px; }
  .brand-square { width: 28px; height: 28px; background: var(--brand-blue); }
  .brand-name { font-family: "Montserrat", sans-serif; font-weight: 700; font-size: 15px; line-height: 1.05; color: var(--brand-blue); letter-spacing: 0.5px; }

  .main-nav { position: absolute; top: 28px; left: 624px; display: flex; font-family: "Montserrat", sans-serif; font-weight: 600; font-size: 12px; color: var(--white); letter-spacing: 0.3px; }
  .main-nav a { color: inherit; text-decoration: none; margin-right: 21px; }
  .main-nav a:nth-child(3) { margin-right: 20px; }
  .donate-btn { position: absolute; left: 921px; top: 23px; width: 105px; height: 26px; background: var(--brand-blue); color: var(--white); font-family: "Montserrat", sans-serif; font-weight: 700; font-size: 8px; letter-spacing: 0.8px; display: flex; align-items: center; justify-content: center; text-decoration: none; }

  .page-title { position: absolute; left: 172px; top: 166px; font-family: "Montserrat", sans-serif; font-weight: 800; font-size: 43px; color: var(--white); letter-spacing: -0.5px; }

  .content { position: absolute; left: 173px; top: 362px; width: 800px; color: var(--body-text); font-size: 11px; line-height: 15px; }
  .content p + p { margin-top: 15px; }
  .funding-heading { position: absolute; left: 174px; top: 442px; font-family: "Montserrat", sans-serif; font-weight: 400; font-size: 16.5px; color: var(--heading-blue); }
  .categories { position: absolute; left: 173px; top: 479px; list-style: none; display: grid; grid-template-columns: 212px 200px; row-gap: 5.5px; font-family: "Montserrat", sans-serif; font-weight: 500; font-size: 11px; color: var(--ink); }
  .categories li { display: flex; align-items: center; gap: 6px; height: 16px; }
  .categories svg { flex: none; }
  .closing { position: absolute; left: 173px; top: 557px; width: 800px; color: var(--body-text); font-size: 11px; line-height: 15.5px; }

  .site-footer { position: absolute; left: 0; top: 659px; width: 1200px; height: 136px; background: var(--footer-bg); color: var(--white); }
  .footer-nav { position: absolute; top: 27px; width: 100%; text-align: center; font-size: 11px; }
  .footer-nav a { color: var(--white); text-decoration: none; }
  .footer-nav .sep { margin: 0 6px; }
  .social { position: absolute; top: 56px; left: 557px; display: flex; gap: 3px; }
  .social span { width: 27px; height: 27px; border-radius: 50%; background: var(--white); display: block; }
  .footer-rule { position: absolute; left: 173px; top: 102px; width: 854px; height: 1px; background: var(--footer-rule); }
  .copyright { position: absolute; top: 114px; width: 100%; text-align: center; font-family: "Montserrat", sans-serif; font-size: 9.5px; }
</style>
</head>
<body>
  <div class="hero" role="img" aria-label="Photo of cupped hands holding a paper cut-out family"></div>
  <svg class="header-panel" viewBox="0 0 420 77" aria-hidden="true"><polygon points="0,0 415,0 372,77 0,77" fill="#ffffff"/></svg>
  <div class="header-rule"></div>

  <a class="brand" href="#">
    <span class="brand-square"></span>
    <span class="brand-name">CORWENNA<br>FOUNDATION</span>
  </a>

  <nav class="main-nav">
    <a href="#">Home</a><a href="#">About us</a><a href="#">Grants</a><a href="#">Contact Us</a>
  </nav>
  <a class="donate-btn" href="#">MAKE DONATION</a>

  <h1 class="page-title">Grants</h1>

  <div class="content">
    <p>Grants will almost entirely be provided for research or education into pain management, or the prevention of pain.</p>
    <p>The trustees will also be providing grants to a number of other charities or to areas with which they have had a long term association, such as HIV/AIDS and TB.<br>There is no application procedure for these other areas, and unsolicited applications are unlikely to be favorably considered by the trustees</p>
  </div>

  <h2 class="funding-heading">The main categories of funding for pain research or education will be as follows.</h2>

  <ul class="categories">
    <li><svg width="12" height="12" viewBox="0 0 12 12"><circle cx="6" cy="6" r="5.3" fill="none" stroke="#1a6fb8" stroke-width="1"/><path d="M4.6 3.4 7.3 6 4.6 8.6" fill="none" stroke="#1a6fb8" stroke-width="1.4"/></svg>Pain centres</li>
    <li><svg width="12" height="12" viewBox="0 0 12 12"><circle cx="6" cy="6" r="5.3" fill="none" stroke="#1a6fb8" stroke-width="1"/><path d="M4.6 3.4 7.3 6 4.6 8.6" fill="none" stroke="#1a6fb8" stroke-width="1.4"/></svg>Education</li>
    <li><svg width="12" height="12" viewBox="0 0 12 12"><circle cx="6" cy="6" r="5.3" fill="none" stroke="#1a6fb8" stroke-width="1"/><path d="M4.6 3.4 7.3 6 4.6 8.6" fill="none" stroke="#1a6fb8" stroke-width="1.4"/></svg>The use of opioids</li>
    <li><svg width="12" height="12" viewBox="0 0 12 12"><circle cx="6" cy="6" r="5.3" fill="none" stroke="#1a6fb8" stroke-width="1"/><path d="M4.6 3.4 7.3 6 4.6 8.6" fill="none" stroke="#1a6fb8" stroke-width="1.4"/></svg>Improved types of pain control</li>
    <li><svg width="12" height="12" viewBox="0 0 12 12"><circle cx="6" cy="6" r="5.3" fill="none" stroke="#1a6fb8" stroke-width="1"/><path d="M4.6 3.4 7.3 6 4.6 8.6" fill="none" stroke="#1a6fb8" stroke-width="1.4"/></svg>Improving the use of medication</li>
    <li><svg width="12" height="12" viewBox="0 0 12 12"><circle cx="6" cy="6" r="5.3" fill="none" stroke="#1a6fb8" stroke-width="1"/><path d="M4.6 3.4 7.3 6 4.6 8.6" fill="none" stroke="#1a6fb8" stroke-width="1.4"/></svg>Measuring pain</li>
  </ul>

  <p class="closing">The trustees will initially consider unsolicited applications, for up to £50,000 each, in these areas or related areas. Applications for more substantial project funding will be invited in due course.</p>

  <footer class="site-footer">
    <nav class="footer-nav">
      <a href="#">Home</a><span class="sep">&nbsp;&nbsp;|</span><a href="#">About</a><span class="sep">|</span><a href="#">Grants</a><span class="sep">&nbsp;|</span><a href="#">Contact</a><span class="sep">&nbsp;|</span><a href="#">Site Map</a>
    </nav>
    <div class="social" aria-label="Social links"><span></span><span></span><span></span></div>
    <div class="footer-rule"></div>
    <p class="copyright">© Corwenna Foundation 2021. All Rights Reserved.</p>
  </footer>
</body>
</html>
```